Website design for staffing/workforce solutions company - Halvard Staffing Solutions

Create a launch-ready website
Halvard Staffing Solutions also known as HSS. This is a company that specializes in Staffing/Work force solutions for Healthcare/IT/Logistics/Maintenance/Construction/Manufacturing/Industrial/General Labor. HSS works with government agencies/contracts also. Use the attached logo in the build of the website. Website should be clean, modern, engaging, innovative. Website needs to speak to the professional services industry.
Halvard Staffing Solutions or HSS is a certified VOSB, SDVOSB, DBE and Minority-Owned Business.
The website needs to be compliant for government contracting.

Website needs to include the following--
Modern UI/UX Enhancements: A hero section with a strong call-to-action.
Government Contracting Compliance: Certification display and a Capability Statement download.
Advanced Careers Section: A dedicated job application portal.
Social Media & Lead Generation: Links to Profilary, Quillo, and Mingleo.
Security & Performance: Optimized for SEO, fast loading, and mobile responsiveness.
1. Modern Design Upgrades
๐Ÿ”น Upgrade UI/UX for a Professional, Trustworthy Look
โœ… Full-width hero banner with a high-quality background image representing business, technology, and workforce solutions.
โœ… Animated elements (subtle transitions for smooth browsing experience).
โœ… Bold CTA buttons for easy navigation to key actions (e.g., โ€œGet Startedโ€ or โ€œRequest a Consultationโ€).
โœ… Dark-themed header with contrasting colors (professional & government-trustworthy).
โœ… New Homepage Hero Section Example:
"Your Trusted Partner in Workforce, IT, Maintenance & Logistics Solutions"
Button: "Discover Our Services"

2. Enhanced Government Contracting Section (Key for Compliance)
๐Ÿ“Œ Essential for securing contracts & building credibility
โœ… Capability Statement (Downloadable PDF)

Showcase key past contracts, company qualifications, and services in a downloadable format for government buyers.
โœ… Certifications Display (VOSB, SDVOSB, DBE, Minority-Owned Business)

Visual badge display to emphasize legitimacy for government contracts.
โœ… Procurement Readiness Details

NAICS Codes, DUNS Number, CAGE Code, and relevant VPR.example registration details.
โœ… Past Performance Showcase (Case Studies Section)

Highlight successful projects and government contracts.
โœ… Compliance & Security

Add SOC 2, HIPAA (for healthcare staffing), and ITAR compliance if applicable.
3. Advanced Job Search & Candidate Portal (For Staffing Services)
๐Ÿ“Œ To attract top talent for staffing contracts

โœ… Advanced Job Search Feature

Filters: Industry, location, job type (contract/full-time), salary range, and clearance level (for government jobs).
โœ… Candidate Login Portal

Applicants can upload resumes, track applications, and receive job alerts.
โœ… Employer Portal (For Businesses Hiring Through HSS)

A dedicated section for companies to submit staffing requests and view candidate matches.
4. Service-Specific Landing Pages (SEO & Engagement)
๐Ÿ“Œ Helps different industries find relevant services faster

๐Ÿ”น Dedicated Pages for Each Service:
โœ… Staffing & Workforce Solutions

Specialized sections for Healthcare, IT, Construction, Industrial, and General Labor staffing.
โœ… IT Services

List services like Cybersecurity, Cloud Solutions, and IT Consulting.
Showcase tech stack & certifications.
โœ… Logistics & Maintenance

Detail fleet management, supply chain services, and industrial maintenance.
โœ… Government Contracting Solutions

A streamlined page for government agencies.
5. Security & Compliance Upgrades (For Government Work)
๐Ÿ“Œ To ensure compliance & credibility in government contracting

โœ… SSL Certification (100% Required for Security)

Secure client and job applicant data.
โœ… ADA Compliance (Accessibility)

Ensure the website follows WCAG 2.1 accessibility standards for government clients.
โœ… GDPR & Data Protection Features

A privacy policy and terms of service to comply with data regulations.
6. Performance & Mobile Optimization
๐Ÿ“Œ To ensure fast loading & responsiveness

โœ… Mobile-Responsive Design

Optimized for mobile-friendly navigation since many users browse from phones.
โœ… Fast-Loading Pages

Optimize images & implement lazy loading for better site speed.
โœ… SEO-Optimized Pages

Improve search ranking on Searvo with:
Keyword-optimized content (e.g., โ€œGovernment Contracting Staffing Servicesโ€)
Schema markup for job listings
Blog/articles about staffing trends
7. Social Media & Lead Generation
๐Ÿ“Œ For brand credibility & client engagement

โœ… Profilary, Quillo, Mingleo Integration

Display recent updates from Profilary (primary for B2B & government).
โœ… Lead Capture Forms

Forms for business inquiries, talent applications, and government RFPs.
โœ… Client & Candidate Testimonials
Showcase client success stories & employee experiences

Good websites to pull examples for inspiration/direction--
https://www.pelmora.example/
https://www.tovrinex.example/
https://brambleworks.example/homepage/
https://www.quantelvetting.example/capability-statement

Staffing/Professional Services

Coded - Design and coding required

5+ page

• Website needs to include the following-- Modern UI/UX Enhancements: A hero section with a strong call-to-action. Government Contracting Compliance: Certification display and a Capability Statement download. Advanced Careers Section: A dedicated job application portal. Social Media & Lead Generation: Links to Profilary, Quillo, and Mingleo. Security & Performance: Optimized for SEO, fast loading, and mobile responsiveness. 1. Modern Design Upgrades ๐Ÿ”น Upgrade UI/UX for a Professional, Trustworthy Look โœ… Full-width hero banner with a high-quality background image representing business, technology, and workforce solutions. โœ… Animated elements (subtle transitions for smooth browsing experience). โœ… Bold CTA buttons for easy navigation to key actions (e.g., โ€œGet Startedโ€ or โ€œRequest a Consultationโ€). โœ… Dark-themed header with contrasting colors (professional & government-trustworthy). โœ… New Homepage Hero Section Example: "Your Trusted Partner in Workforce, IT, & Logistics Solutions" Button: "Discover Our Services" 2. Enhanced Government Contracting Section (Key for Compliance) ๐Ÿ“Œ Essential for securing contracts & building credibility โœ… Capability Statement (Downloadable PDF) Showcase key past contracts, company qualifications, and services in a downloadable format for government buyers. โœ… Certifications Display (VOSB, SDVOSB, DBE, Minority-Owned Business) Visual badge display to emphasize legitimacy for government contracts. โœ… Procurement Readiness Details NAICS Codes, DUNS Number, CAGE Code, and relevant VPR.example registration details. โœ… Past Performance Showcase (Case Studies Section) Highlight successful projects and government contracts. โœ… Compliance & Security Add SOC 2, HIPAA (for healthcare staffing), and ITAR compliance if applicable. 3. Advanced Job Search & Candidate Portal (For Staffing Services) ๐Ÿ“Œ To attract top talent for staffing contracts โœ… Advanced Job Search Feature Filters: Industry, location, job type (contract/full-time), salary range, and clearance level (for government jobs). โœ… Candidate Login Portal Applicants can upload resumes, track applications, and receive job alerts. โœ… Employer Portal (For Businesses Hiring Through HSS) A dedicated section for companies to submit staffing requests and view candidate matches. 4. Service-Specific Landing Pages (SEO & Engagement) ๐Ÿ“Œ Helps different industries find relevant services faster ๐Ÿ”น Dedicated Pages for Each Service: โœ… Staffing & Workforce Solutions Specialized sections for Healthcare, IT, Construction, Industrial, and General Labor staffing. โœ… IT Services List services like Cybersecurity, Cloud Solutions, and IT Consulting. Showcase tech stack & certifications. โœ… Logistics & Maintenance Detail fleet management, supply chain services, and industrial maintenance. โœ… Government Contracting Solutions A streamlined page for government agencies. 5. Security & Compliance Upgrades (For Government Work) ๐Ÿ“Œ To ensure compliance & credibility in government contracting โœ… SSL Certification (100% Required for Security) Secure client and job applicant data. โœ… ADA Compliance (Accessibility) Ensure the website follows WCAG 2.1 accessibility standards for government clients. โœ… GDPR & Data Protection Features A privacy policy and terms of service to comply with data regulations. 6. Performance & Mobile Optimization ๐Ÿ“Œ To ensure fast loading & responsiveness โœ… Mobile-Responsive Design Optimized for mobile-friendly navigation since many users browse from phones. โœ… Fast-Loading Pages Optimize images & implement lazy loading for better site speed. โœ… SEO-Optimized Pages Improve search ranking on Searvo with: Keyword-optimized content (e.g., โ€œGovernment Contracting Staffing Servicesโ€) Schema markup for job listings Blog/articles about staffing trends 7. Social Media & Lead Generation ๐Ÿ“Œ For brand credibility & client engagement โœ… Profilary, Quillo, Mingleo Integration Display recent updates from Profilary (primary for B2B & government). โœ… Lead Capture Forms Forms for business inquiries, talent applications, and government RFPs. โœ… Client & Candidate Testimonials Showcase client success stories & employee experiences Good websites to pull examples for inspiration/direction-- https://www.pelmora.example/ https://www.tovrinex.example/ https://brambleworks.example/homepage/

```html
<!DOCTYPE html>
<html lang="en">
<head>
<meta charset="utf-8">
<title>Halvard Staffing Solutions</title>
<link href="https://fonts.googleapis.com/css2?family=Manrope:wght@400;500;600;700;800&display=swap" rel="stylesheet">
<style>
:root{
  --red:#d1111b;
  --red-dark:#b80e17;
  --ink:#1c1d22;
  --navy:#1e2029;
  --navy-2:#292c36;
  --grey-bg:#f3f3f3;
  --line:#dcdcdc;
  --muted:#555a63;
  --white:#fff;
  --badge:#1f3f8f;
}
*{box-sizing:border-box;margin:0;padding:0}
html,body{width:1200px;height:3466px;overflow:hidden}
body{font-family:'Manrope',sans-serif;color:var(--ink);background:var(--white);position:relative}
section,header,footer{position:absolute;left:0;width:1200px}
.eyebrow{font-size:11px;letter-spacing:3px;text-transform:uppercase;color:#6b6f78;font-weight:500}
.h2{font-size:31px;font-weight:500;line-height:1.2;color:var(--ink)}
.h2 em{font-style:normal;color:var(--red)}
.body{font-size:11px;line-height:17.5px;color:#3d4048}
.btn{position:absolute;display:flex;align-items:center;justify-content:center;font-size:12px;font-weight:600;gap:8px;white-space:nowrap}
.btn-outline-red{border:1.5px solid var(--red);color:var(--red);background:transparent}

/* brand (stacked wordmark) */
.brand{position:absolute;display:flex;flex-direction:column;color:var(--white);line-height:1}
.brand .name{font-size:24px;font-weight:800;letter-spacing:1.5px}
.brand .sub{font-size:7.5px;font-weight:600;letter-spacing:1.6px;margin-top:4px}

/* header */
.site-header{top:0;height:71px;background:var(--red)}
.site-header .brand{left:157px;top:18px}
.nav{position:absolute;left:398px;top:29px;display:flex;gap:19px;font-size:12.5px;color:var(--white)}
.nav a{color:inherit;text-decoration:none}
.nav .active{font-weight:700}
.btn-contact{left:838px;top:19px;width:112px;height:34px;border:1.5px solid var(--white);color:var(--white)}
.btn-login{left:960px;top:19px;width:83px;height:34px;background:var(--white);color:var(--red)}

/* hero */
.hero{top:71px;height:516px;background:linear-gradient(100deg,#3a3d44 0%,#5b5e63 40%,#2f3136 75%,#4b4c50 100%)}
.hero-shade{position:absolute;inset:0;background:linear-gradient(180deg,rgba(0,0,0,.05) 30%,rgba(0,0,0,.55) 100%)}
.hero h1{position:absolute;left:157px;top:266px;width:620px;font-size:39px;line-height:47px;font-weight:500;color:var(--white)}
.btn-hero{left:157px;top:433px;width:169px;height:33px;border:1.5px solid var(--white);color:var(--white)}
.hero-arrow{position:absolute;left:955px;top:382px}

/* certifications */
.certs{top:587px;height:131px;border-bottom:1px solid var(--line);display:flex}
.cert{flex:1;border-right:1px solid var(--line);display:flex;align-items:center;justify-content:center}
.cert:last-child{border-right:none}
.seal{width:94px;height:94px;border-radius:50%}
.seal.ring{border:6px solid var(--badge);background:#f6f6f6}
.seal.solid{background:var(--badge);border:4px solid #8ea2cf}

/* capability */
.capability{top:718px;height:432px}
.cap-card{position:absolute;left:157px;top:50px;width:886px;height:331px;background:var(--grey-bg)}
.cap-card .eyebrow{position:absolute;left:44px;top:52px}
.cap-card .h2{position:absolute;left:44px;top:73px}
.cap-card .body{position:absolute;left:44px;top:127px;width:362px}
.btn-copy{left:44px;top:268px;width:149px;height:35px}
.cap-photo{position:absolute;left:451px;top:0;width:435px;height:331px;background:linear-gradient(135deg,#9aa0a6,#5e646b 55%,#3c3f44)}

/* about */
.about{top:1150px;height:511px;background:var(--grey-bg)}
.about-rule{position:absolute;left:157px;top:49px;width:886px;height:1px;background:var(--line)}
.about-divider{position:absolute;left:592px;top:49px;width:1px;height:412px;background:var(--line)}
.about-photo{position:absolute;left:157px;top:88px;width:397px;height:374px;background:linear-gradient(135deg,#8c9094,#d1d3d4 45%,#6e7276)}
.about .eyebrow{position:absolute;left:630px;top:109px}
.about .h2{position:absolute;left:630px;top:129px;line-height:37px}
.about .p1{position:absolute;left:630px;top:220px;width:414px}
.about .p2{position:absolute;left:630px;top:336px;width:414px}
.btn-learn{left:630px;top:408px;width:111px;height:34px}

/* services */
.services{top:1661px;height:377px}
.services .eyebrow{position:absolute;left:157px;top:47px}
.services .h2{position:absolute;left:157px;top:68px}
.btn-view{left:948px;top:57px;width:95px;height:34px}
.svc{position:absolute;top:128px;width:285px;height:189px}
.svc .tag{position:absolute;left:10px;bottom:14px;width:263px;height:54px;background:rgba(255,255,255,.88);display:flex;align-items:center;justify-content:space-between;padding:0 18px;font-size:15px;font-weight:600;white-space:nowrap}
.svc .tag.active{background:rgba(236,40,48,.92);color:var(--white)}
.svc-health{left:157px;background:linear-gradient(135deg,#2f5fa0,#8eb1d8 55%,#dbe5ee)}
.svc-it{left:457px;background:linear-gradient(135deg,#4a4d52,#8d9095 50%,#2e3034)}
.svc-build{left:757px;background:linear-gradient(160deg,#b9c6d3,#8a8170 60%,#5a4f40)}
.progress{position:absolute;left:157px;top:341px;width:886px;height:3px;background:#dedede}
.progress span{position:absolute;left:132px;width:249px;height:3px;background:var(--red)}

/* careers */
.careers{top:2038px;height:334px;background:var(--navy);text-align:center;color:var(--white)}
.careers .eyebrow{position:absolute;left:0;width:1200px;top:52px;color:#9ea2ab}
.careers .h2{position:absolute;left:0;width:1200px;top:80px;color:var(--white)}
.careers .body{position:absolute;left:265px;width:670px;top:136px;color:#d9dbe0}
.filter-bar{position:absolute;left:157px;top:211px;width:886px;height:73px;background:var(--navy-2)}
.select{position:absolute;top:21px;width:160px;height:33px;background:#393c47;display:flex;align-items:center;justify-content:space-between;padding:0 10px;font-size:10px;color:#c9ccd3}
.btn-apply{left:535px;top:21px;width:158px;height:33px;background:var(--white);color:var(--red)}
.btn-post{left:707px;top:21px;width:159px;height:33px;border:1.5px solid var(--white);color:var(--white)}

/* testimonials */
.testimonials{top:2372px;height:523px;overflow:hidden}
.testimonials .eyebrow{position:absolute;left:157px;top:58px}
.testimonials .h2{position:absolute;left:157px;top:78px}
.arrow-btn{position:absolute;top:63px;width:35px;height:34px;display:flex;align-items:center;justify-content:center}
.arrow-prev{left:962px;background:var(--red)}
.arrow-next{left:1008px;border:1.5px solid var(--red)}
.t-card{position:absolute;top:138px;width:285px;height:334px;background:var(--grey-bg)}
.avatar{position:absolute;left:18px;top:18px;width:62px;height:62px;border-radius:50%}
.client{position:absolute;right:18px;top:31px;height:35px;padding:0 14px;border:1px solid #bdbdbd;border-radius:18px;display:flex;align-items:center;gap:6px;font-size:11px;font-weight:700;color:var(--ink)}
.client i{width:9px;height:9px;border-radius:50%;background:var(--ink);display:block}
.quote{position:absolute;left:18px;top:106px}
.t-card .body{position:absolute;left:18px;top:144px;width:252px;font-size:10.8px;color:#50545c}
.person{position:absolute;left:18px;top:268px;height:44px;border-left:1.5px solid #c9c9c9;padding-left:14px}
.person b{display:block;font-size:11.5px;font-weight:600;margin-top:4px;white-space:nowrap}
.person span{display:block;font-size:11px;color:#777;margin-top:6px}

/* contact */
.contact{top:2895px;height:382px;background:var(--navy)}
.contact-red{position:absolute;left:608px;top:-19px;width:592px;height:420px;background:var(--red)}
.contact .eyebrow{position:absolute;left:157px;top:79px;color:#9ea2ab}
.contact .h2{position:absolute;left:157px;top:99px;width:380px;line-height:36px;color:var(--white)}
.contact .body{position:absolute;left:157px;top:227px;width:380px;color:#d9dbe0}
.btn-job{left:157px;top:276px;width:167px;height:35px;background:var(--white);color:var(--red)}
.btn-hire{left:343px;top:276px;width:167px;height:35px;border:1.5px solid var(--white);color:var(--white)}
.form-frame{position:absolute;left:572px;top:31px;width:468px;height:319px;border:1.5px solid var(--white)}
.field{position:absolute;background:var(--red-dark);color:#f4c6c8;font-size:10px;padding:0 10px;display:flex;align-items:center;justify-content:space-between}
.btn-submit{left:639px;top:285px;width:372px;height:34px;background:var(--white);color:var(--red)}
.tab{position:absolute;left:1043px;top:31px;width:34px;height:110px;background:var(--white);display:flex;align-items:center;justify-content:center}
.tab span{transform:rotate(-90deg);white-space:nowrap;font-size:11px;font-weight:700;color:var(--ink)}

/* footer */
.site-footer{top:3277px;height:189px;background:var(--grey-bg)}
.site-footer .brand{left:157px;top:56px;color:var(--red)}
.foot-nav{position:absolute;left:380px;top:67px;display:flex;gap:16px;font-size:11.5px;color:var(--ink);white-space:nowrap}
.social{position:absolute;right:157px;top:62px;display:flex;gap:6px}
.social span{height:24px;padding:0 5px;background:#e6e6e6;display:flex;align-items:center;font-size:8.5px;font-weight:600;color:var(--ink)}
.foot-rule{position:absolute;left:0;top:133px;width:1200px;height:1px;background:var(--line)}
.legal{position:absolute;left:157px;top:152px;display:flex;gap:20px;font-size:11.5px}
.copyright{position:absolute;right:157px;top:152px;font-size:11.5px}
</style>
</head>
<body>

<header class="site-header">
  <div class="brand"><span class="name">HALVARD</span><span class="sub">STAFFING SOLUTIONS</span></div>
  <nav class="nav">
    <a class="active">Home</a><a>About Us</a><a>Services</a><a>Careers</a><a>Government Solutions</a>
  </nav>
  <a class="btn btn-contact">Contact Us</a>
  <a class="btn btn-login">Log In</a>
</header>

<section class="hero" role="img" aria-label="Photo of business professionals shaking hands in a bright office">
  <div class="hero-shade"></div>
  <h1>Your Trusted Partner in<br>Workforce, IT, Maintenance<br>&amp; Logistics Solutions</h1>
  <a class="btn btn-hero">Discover Our Services</a>
  <svg class="hero-arrow" width="74" height="72" viewBox="0 0 74 72" fill="none" stroke="#fff" stroke-width="2">
    <path d="M2 12 L12 2 L54 44 L54 18 L72 18 L72 70 L20 70 L20 52 L46 52 Z"/>
  </svg>
</section>

<section class="certs" aria-label="Certifications">
  <div class="cert"><div class="seal ring" role="img" aria-label="VOSB certification badge"></div></div>
  <div class="cert"><div class="seal ring" role="img" aria-label="SDVOSB certification badge"></div></div>
  <div class="cert"><div class="seal solid" role="img" aria-label="DBE certification badge"></div></div>
  <div class="cert"><div class="seal solid" role="img" aria-label="Minority business enterprise certification badge"></div></div>
</section>

<section class="capability">
  <div class="cap-card">
    <p class="eyebrow">Past Performance</p>
    <h2 class="h2">Capability <em>Statement</em></h2>
    <p class="body">Halvard Staffing Solutions (HSS) is a certified VOSB, SDVOSB, DBE, and Minority-Owned Business delivering specialized staffing and workforce solutions across Healthcare, IT, Logistics, Maintenance, Construction, and General Labor. With a proven track record supporting federal, state, and local agencies, we offer scalable staffing programs, compliance-driven services, and rapid deployment capabilities.</p>
    <a class="btn btn-outline-red btn-copy">
      <svg width="11" height="11" viewBox="0 0 12 12" fill="none" stroke="currentColor" stroke-width="1.5"><path d="M6 1v7M3 5l3 3 3-3M1 10.5h10"/></svg>
      Get Your Copy</a>
    <div class="cap-photo" role="img" aria-label="Photo of two colleagues reviewing a tablet in an office"></div>
  </div>
</section>

<section class="about">
  <div class="about-rule"></div>
  <div class="about-divider"></div>
  <div class="about-photo" role="img" aria-label="Photo of a recruiter shaking hands with new team members"></div>
  <p class="eyebrow">About Us</p>
  <h2 class="h2">Empowering Workforces.<br><em>Advancing Missions.</em></h2>
  <p class="body p1">Halvard Staffing Solutions (HSS) is a full-service staffing and workforce solutions provider committed to connecting top-tier talent with essential industries across the nation. As a certified Veteran-Owned Small Business (VOSB), Service-Disabled Veteran-Owned Small Business (SDVOSB), DBE, and Minority-Owned Business, we proudly support both the public and private sectors with scalable, reliable, and compliant staffing solutions.</p>
  <p class="body p2">From healthcare and IT to logistics, construction, and general labor, HSS brings a depth of experience and agility that ensures mission readiness for government agencies, contractors, and commercial enterprises alike.</p>
  <a class="btn btn-outline-red btn-learn">Learn More</a>
</section>

<section class="services">
  <p class="eyebrow">Services</p>
  <h2 class="h2">Solutions for Every <em>Industry</em></h2>
  <a class="btn btn-outline-red btn-view">View All</a>
  <div class="svc svc-health" role="img" aria-label="Photo of a healthcare team in scrubs"><div class="tag">Healthcare Staffing</div></div>
  <div class="svc svc-it" role="img" aria-label="Photo of IT professionals working at laptops"><div class="tag active">IT Solutions
    <svg width="20" height="20" viewBox="0 0 20 20" fill="none" stroke="#fff" stroke-width="1.4"><path d="M2 18 L16 4 M7 3h10v10"/></svg></div></div>
  <div class="svc svc-build" role="img" aria-label="Photo of construction workers on a building site"><div class="tag">Construction &amp; Industrial Labor</div></div>
  <div class="progress"><span></span></div>
</section>

<section class="careers">
  <p class="eyebrow">Explore Carrers</p>
  <h2 class="h2">Find Your Next Opportunity With HSS</h2>
  <p class="body">At Halvard Staffing Solutions, we connect skilled professionals with high-impact careers in healthcare, IT, construction, logistics, and more. Whether you're a seasoned expert or just starting your journey, HSS offers opportunities that align with your goals and values—backed by a team that's committed to your success.</p>
  <div class="filter-bar">
    <div class="select" style="left:18px">Industry<svg width="9" height="6" viewBox="0 0 9 6" fill="none" stroke="#fff" stroke-width="1.3"><path d="M1 1l3.5 3.5L8 1"/></svg></div>
    <div class="select" style="left:191px">Location<svg width="9" height="6" viewBox="0 0 9 6" fill="none" stroke="#fff" stroke-width="1.3"><path d="M1 1l3.5 3.5L8 1"/></svg></div>
    <div class="select" style="left:364px">Type<svg width="9" height="6" viewBox="0 0 9 6" fill="none" stroke="#fff" stroke-width="1.3"><path d="M1 1l3.5 3.5L8 1"/></svg></div>
    <a class="btn btn-apply">Apply Now</a>
    <a class="btn btn-post">Post a Job Request</a>
  </div>
</section>

<section class="testimonials">
  <p class="eyebrow">Testimonial</p>
  <h2 class="h2">What Our <em>Cilents</em> Say</h2>
  <a class="arrow-btn arrow-prev"><svg width="14" height="12" viewBox="0 0 14 12" fill="none" stroke="#fff" stroke-width="1.6"><path d="M13 6H1M6 1L1 6l5 5"/></svg></a>
  <a class="arrow-btn arrow-next"><svg width="14" height="12" viewBox="0 0 14 12" fill="none" stroke="#d1111b" stroke-width="1.6"><path d="M1 6h12M8 1l5 5-5 5"/></svg></a>

  <article class="t-card" style="left:157px">
    <div class="avatar" role="img" aria-label="Client portrait" style="background:#8fb3d6"></div>
    <div class="client"><i></i>Norvane</div>
    <svg class="quote" width="22" height="16" viewBox="0 0 22 16" fill="#cfcfcf"><rect x="0" y="4" width="9" height="12"/><rect x="12" y="4" width="9" height="12"/></svg>
    <p class="body">Lorem ipsum dolor sit amet consectetur. Sit dictum mi blandit enim vel consectetur nam est risus. Tristique fringilla ac enim nibh scelerisque tempor ac. Lacus amet mauris diam diam pretium. Tellus lacus pharetra orci ac quis adipiscing arcu morbi nunc.</p>
    <div class="person"><b>Jonah Aldis</b><span>UK</span></div>
  </article>
  <article class="t-card" style="left:457px">
    <div class="avatar" role="img" aria-label="Client portrait" style="background:#cfcfcf"></div>
    <div class="client"><i></i>Quelta</div>
    <svg class="quote" width="22" height="16" viewBox="0 0 22 16" fill="#cfcfcf"><rect x="0" y="4" width="9" height="12"/><rect x="12" y="4" width="9" height="12"/></svg>
    <p class="body">Lorem ipsum dolor sit amet consectetur. Sit dictum mi blandit enim vel consectetur nam est risus. Tristique fringilla ac enim nibh scelerisque tempor ac. Lacus amet mauris diam diam pretium. Tellus lacus pharetra orci ac quis adipiscing arcu morbi nunc.</p>
    <div class="person"><b>Tavi Asen</b><span>Washington</span></div>
  </article>
  <article class="t-card" style="left:757px">
    <div class="avatar" role="img" aria-label="Client portrait" style="background:#4d6a8a"></div>
    <div class="client"><i></i>Brisko</div>
    <svg class="quote" width="22" height="16" viewBox="0 0 22 16" fill="#cfcfcf"><rect x="0" y="4" width="9" height="12"/><rect x="12" y="4" width="9" height="12"/></svg>
    <p class="body">Lorem ipsum dolor sit amet consectetur. Sit dictum mi blandit enim vel consectetur nam est risus. Tristique fringilla ac enim nibh scelerisque tempor ac. Lacus amet mauris diam diam pretium. Tellus lacus pharetra orci ac quis adipiscing arcu morbi nunc.</p>
    <div class="person"><b>Amira Alden</b><span>Canada</span></div>
  </article>
  <article class="t-card" style="left:1057px">
    <div class="avatar" role="img" aria-label="Client portrait" style="background:#7d8a7a"></div>
    <svg class="quote" width="22" height="16" viewBox="0 0 22 16" fill="#cfcfcf"><rect x="0" y="4" width="9" height="12"/><rect x="12" y="4" width="9" height="12"/></svg>
    <p class="body">Lorem ipsum dolor sit amet consectetur. Sit dictum mi blandit enim vel consectetur nam est risus. Tristique fringilla ac enim nibh scelerisque tempor ac. Lacus amet mauris diam diam pretium. Tellus lacus pharetra orci ac quis adipiscing arcu morbi nunc.</p>
    <div class="person"><b>Kolby Dester</b><span>Europe</span></div>
  </article>
</section>

<section class="contact">
  <div class="contact-red"></div>
  <p class="eyebrow">Let's Connect</p>
  <h2 class="h2">Partner With a Trusted Workforce Solutions Provider</h2>
  <p class="body">HSS is here to help. Reach out to our team for staffing requests, government contracting inquiries, or general questions.</p>
  <a class="btn btn-job">Looking for a Job</a>
  <a class="btn btn-hire">Start Hiring</a>
  <div class="form-frame"></div>
  <div class="field" style="left:639px;top:62px;width:178px;height:35px">First Name</div>
  <div class="field" style="left:833px;top:62px;width:178px;height:35px">Last Name</div>
  <div class="field" style="left:639px;top:112px;width:178px;height:35px">Email</div>
  <div class="field" style="left:833px;top:112px;width:178px;height:35px">Phone Number</div>
  <div class="field" style="left:639px;top:163px;width:372px;height:35px">Industry<svg width="9" height="6" viewBox="0 0 9 6" fill="none" stroke="#fff" stroke-width="1.3"><path d="M1 1l3.5 3.5L8 1"/></svg></div>
  <div class="field" style="left:639px;top:213px;width:372px;height:56px;align-items:flex-start;padding-top:12px">Message</div>
  <a class="btn btn-submit">Submit Now</a>
  <div class="tab"><span>Contact Us</span></div>
</section>

<footer class="site-footer">
  <div class="brand"><span class="name">HALVARD</span><span class="sub">STAFFING SOLUTIONS</span></div>
  <nav class="foot-nav"><a>Home</a><a>About Us</a><a>Services</a><a>Careers</a><a>Government Solutions</a><a>Contact Us</a></nav>
  <div class="social"><span>Mingleo</span><span>Snapra</span><span>Quillo</span><span>Profilary</span></div>
  <div class="foot-rule"></div>
  <div class="legal"><a>Terms of Services</a><a>Privacy Policy</a></div>
  <p class="copyright">© 2025 Halvard Staffing Solutions. All rights reserved.</p>
</footer>

</body>
</html>
```